Rack Card Design Project

We are a locally family owned public golf course. We would like to have a rack card designed that can be used for multiple applications. The colors in our logo are grey, blue, and white. Please use those in the card design. The company logo, contact information, address, and summer pricing should be included. I've included some pictures that may or may not be used. I'm also open to suggestions....use one photo, multiple photos, a stock photo or image representing golf etc.

```html
<!DOCTYPE html>
<html lang="en">
<head>
<meta charset="utf-8">
<title>Summer Rates Rack Card</title>
<link href="https://fonts.googleapis.com/css2?family=Crimson+Text:wght@400;600;700&display=swap" rel="stylesheet">
<style>
  :root {
    --navy: #14365f;
    --navy-deep: #0f2d52;
    --sky-row: #c4e6fb;
    --grey: #8a8a8c;
    --grey-light: #a7a7a9;
    --white: #ffffff;
    --ink: #1c1c1c;
  }
  * { box-sizing: border-box; margin: 0; padding: 0; }
  html, body { width: 672px; height: 1200px; overflow: hidden; background: var(--white); }
  body { font-family: "Crimson Text", Georgia, serif; color: var(--ink); }
  .rack-card { position: relative; width: 672px; height: 1200px; overflow: hidden; background: var(--white); }

  .hero { position: absolute; left: 0; top: 0; width: 672px; height: 460px; }
  .hero svg { display: block; }

  .club-name {
    position: absolute; left: 40px; top: 60px; width: 250px;
    display: flex; align-items: center; gap: 14px;
    font-weight: 700; font-size: 30px; line-height: 1.05; color: var(--white);
  }
  .club-name .dot { flex: 0 0 30px; height: 30px; border-radius: 50%; background: var(--grey-light); }

  .photo-circle {
    position: absolute; border-radius: 50%;
    border: 4px solid var(--navy);
    box-shadow: 0 4px 8px rgba(0,0,0,.3);
  }
  .photo-circle.left { left: 34px; top: 380px; width: 206px; height: 206px;
    background: linear-gradient(180deg, #9fc0dc 0%, #d7dde0 45%, #3f6d2c 62%, #2d5220 100%); }
  .photo-circle.middle { left: 292px; top: 432px; width: 206px; height: 206px;
    background: radial-gradient(circle at 70% 25%, #fff4d6 0%, #c9c08a 25%, #6f8c3c 60%, #3b5a23 100%); }
  .photo-circle.right { left: 492px; top: 392px; width: 150px; height: 150px;
    background: linear-gradient(180deg, #b7c3cf 0%, #e9d6b7 40%, #4a6a32 62%, #2f4a20 100%); }

  .rates-title {
    position: absolute; left: 0; top: 640px; width: 672px; text-align: center;
    font-size: 58px; font-weight: 600; color: var(--navy); line-height: 1;
  }
  .season {
    position: absolute; left: 120px; top: 700px; width: 432px; height: 44px;
    border-radius: 22px; background: var(--grey); color: var(--white);
    font-size: 30px; text-align: center; line-height: 44px;
  }

  .rate-table {
    position: absolute; left: 82px; top: 764px; width: 492px;
    border-collapse: separate; border-spacing: 0 3px;
    box-shadow: 8px 8px 10px rgba(0,0,0,.25);
    font-size: 23px;
  }
  .rate-table td { height: 34px; padding: 0 14px; }
  .rate-table td.price { width: 118px; text-align: center; font-weight: 700; border-left: 3px solid var(--white); }
  .rate-table tr.heading td { background: var(--navy); color: var(--white); font-weight: 600; }
  .rate-table tr.tier td { background: var(--sky-row); color: var(--navy-deep); font-weight: 600; }

  .lunch {
    position: absolute; left: 120px; top: 1002px; width: 432px; height: 40px;
    border-radius: 20px; background: var(--grey); color: var(--white);
    font-size: 21px; font-weight: 700; text-align: center; line-height: 40px;
  }

  .footer { position: absolute; left: 0; top: 1020px; width: 672px; height: 180px; }
  .footer-wave { position: absolute; left: 0; top: 0; }
  .contact { position: absolute; left: 0; top: 40px; width: 672px; text-align: center; color: var(--white); }
  .contact p { display: flex; justify-content: center; align-items: center; gap: 8px; line-height: 1; }
  .contact .name { font-size: 21px; font-weight: 700; margin-bottom: 14px; }
  .contact .address { font-size: 20px; margin-bottom: 12px; }
  .contact .phone { font-size: 24px; font-weight: 700; margin-bottom: 9px; }
  .contact .web { font-size: 25px; }
  .icon { display: block; width: 22px; height: 22px; flex: 0 0 22px; }
</style>
</head>
<body>
<main class="rack-card">
  <div class="hero">
    <svg width="672" height="460" viewBox="0 0 672 460">
      <defs>
        <linearGradient id="course-scene" x1="0" y1="0" x2="0" y2="1">
          <stop offset="0" stop-color="#3f74c6"/>
          <stop offset="0.45" stop-color="#8fb5dc"/>
          <stop offset="0.58" stop-color="#4c6b3a"/>
          <stop offset="0.75" stop-color="#3c6a26"/>
          <stop offset="1" stop-color="#4e7a2e"/>
        </linearGradient>
      </defs>
      <path role="img" aria-label="Golf course fairway with palm trees under a blue sky"
            d="M0 0 H672 V360 Q336 470 0 360 Z" fill="url(#course-scene)"/>
      <path d="M0 368 Q336 478 672 368" fill="none" stroke="var(--grey-light)" stroke-width="3"/>
    </svg>
  </div>

  <div class="club-name"><span class="dot"></span><span>The Harbors of Pine Creek Golf Club</span></div>

  <div class="photo-circle left" role="img" aria-label="Fairway with trees at sunrise"></div>
  <div class="photo-circle middle" role="img" aria-label="Golf iron and ball on the green in sunlight"></div>
  <div class="photo-circle right" role="img" aria-label="Course trees at sunset"></div>

  <h1 class="rates-title">Summer Rates</h1>
  <div class="season">May 1 – September 30</div>

  <table class="rate-table">
    <tr class="heading"><td>18 Holes With Cart</td><td class="price"></td></tr>
    <tr class="tier"><td>7AM – 11AM</td><td class="price">$24</td></tr>
    <tr class="tier"><td>11AM – 3PM</td><td class="price">$19</td></tr>
    <tr class="tier"><td>3PM – Close</td><td class="price">$15</td></tr>
    <tr class="heading"><td>9 Holes With Cart</td><td class="price">$15</td></tr>
    <tr class="heading"><td>Walking</td><td class="price">$12</td></tr>
  </table>

  <div class="lunch">Lunch Available Daily : 10AM – 3PM</div>

  <footer class="footer">
    <svg class="footer-wave" width="672" height="180" viewBox="0 0 672 180">
      <path d="M0 50 Q300 -5 672 10 V180 H0 Z" fill="var(--grey)"/>
      <path d="M0 64 Q320 8 672 30 V180 H0 Z" fill="var(--navy)"/>
    </svg>
    <div class="contact">
      <p class="name">The Harbors of Pine Creek Golf Club</p>
      <p class="address">
        <svg class="icon" viewBox="0 0 24 24"><circle cx="12" cy="12" r="11" fill="var(--white)"/><path d="M12 5a4.5 4.5 0 0 0-4.5 4.5C7.5 13 12 19 12 19s4.5-6 4.5-9.5A4.5 4.5 0 0 0 12 5zm0 6.2a1.7 1.7 0 1 1 0-3.4 1.7 1.7 0 0 1 0 3.4z" fill="var(--navy)"/></svg>
        4410 SW Cedar Bend Rd Palm Hollow, FL 34001
      </p>
      <p class="phone">
        <svg class="icon" viewBox="0 0 24 24"><circle cx="12" cy="12" r="11" fill="var(--white)"/><path d="M8.6 6.5l1.8 2.6-1.1 1.4c.8 1.7 2 2.9 3.7 3.7l1.4-1.1 2.6 1.8-1 2c-4.6-.3-8.2-3.9-8.5-8.5z" fill="var(--navy)"/></svg>
        555-318-2047
      </p>
      <p class="web">
        <svg class="icon" viewBox="0 0 24 24"><circle cx="12" cy="12" r="11" fill="var(--white)"/><g fill="none" stroke="var(--navy)" stroke-width="1.4"><circle cx="12" cy="12" r="6"/><ellipse cx="12" cy="12" rx="2.6" ry="6"/><path d="M6 12h12"/></g></svg>
        www.pinecreekgc.com
      </p>
    </div>
  </footer>
</main>
</body>
</html>
```